Brantley Estates is a commercial real estate development company based in the United States. We develop high-end office buildings and student housing apartments. We have a new logo and need to update all of our stationary items and business cards. We would like the design to be clean and professional. Our logo and color information is attached. Our logo MUST be in full color and not as white. It is preferred that the logo is on a white background.

Color code Blue R 0. G 62. B 124 ( #003E7C )
C 100 M84 Y 26 K 22
Black R32. G30. B30 ( #201E1E)
C100 M100 Y100 K100

Font used TRAJAN PRO3 PRO BOLD.

Items needed:
1. Business card - Leaning towards doing just a one side business card in a thicker paper. Include - logo, name - Martin E. Caldwell, Title - Chairman & CEO, 5120 Ridgemont Pkwy. Suite 400, Atlanta, GA 30327 - Cell number 404.617.####, Office 770.245.62## email@brantleyestates.com; www.brantleyestates.com.

2. Letterhead - Standard 8.5 by 11 paper. We do have a smaller size for the CEO that is 7.25 by 10.5 that is just a mirror of the letterhead except with his name (Martin E. Caldwell) and title (Chariman & CEO) listed at the top in the header. Letthead needs address, phone number and website, plus logo. *Prepared such that we can either implement as a Google Document template or professionally print.

3. Legal sized envelope - #10 envelope - which measures 4 1/8" by 9 1/2". We also use the same size envelope with a window. Need logo and address. A photo of the old envelope style is attached.

4. 9" x 12" Pocket folder - Need a design that can also be split to be a cover page and back - We use the cover pages in spiral binding machine, so we need to leave room on the left for that. One of the pockets should hold a business card. Include logo, address, phone, website. Also if text is needed, we could say development / leasing / property management.

5. Shipping label - 3 1/3" x 4" inches and 6 per page. Just need logo and address listed at top of the label and white space at bottom.

Company: Brantley Estates
Address: 5120 Ridgemont Pkwy. Suite 400, Atlanta, GA 30327
Phone: 770.245.6274
Fax: 770.245.6219 (probably not needed)
Website: www.brantleyestates.com

Thank you for all your help!

Target Market(s)

Should communicate a strong corporate feel

Contact Information for Business Card

Include - logo, name - Martin E. Caldwell, Title - Chairman & CEO, 5120 Ridgemont Pkwy. Suite 400, Atlanta, GA 30327 - Cell number 404.617.####, Office 770.245.62## email@brantleyestates.com; www.brantleyestates.com.

Logo Text

Brantley Estates

Colors

Designer to choose colors to be used in the design.

Requirements
Must have
• Our logo MUST be in full color and not as white. It is preferred that the logo is on a white background.
• Colors - Color code Blue R 0. G 62. B 124 ( #003E7C )
• C 100 M84 Y 26 K 22
Nice to have
• Font used in logo TRAJAN PRO3 PRO BOLD. Would love to see options of both a one sided and double-sided.
Should not have
• Logo in white.

```html
<!DOCTYPE html>
<html lang="en">
<head>
<meta charset="utf-8">
<title>Brantley Estates – Business Card</title>
<link href="https://fonts.googleapis.com/css2?family=Cinzel:wght@700&family=EB+Garamond:wght@400&display=swap" rel="stylesheet">
<style>
  :root {
    --brand-blue: #163a6e;
    --paper: #ffffff;
    --canvas: #e6e6e6;
    --ink-grey: #555555;
  }
  html, body {
    margin: 0;
    padding: 0;
    width: 1125px;
    height: 1200px;
    overflow: hidden;
    background: var(--canvas);
  }
  .canvas {
    position: relative;
    width: 1125px;
    height: 1200px;
  }
  .card {
    position: absolute;
    left: 171px;
    width: 826px;
    height: 471px;
    background: var(--paper);
    overflow: hidden;
  }
  .card--front { top: 106px; }
  .card--back  { top: 639px; }

  .front-shape {
    position: absolute;
    inset: 0;
    width: 100%;
    height: 100%;
  }
  .contact-block {
    position: absolute;
    left: 45px;
    top: 110px;
    max-width: 300px;
    color: var(--paper);
    font-family: "EB Garamond", Georgia, serif;
  }
  .person-name {
    margin: 0;
    font-family: "Cinzel", "Trajan Pro", serif;
    font-weight: 700;
    font-size: 24px;
    line-height: 1.1;
    letter-spacing: 0;
    white-space: nowrap;
  }
  .person-title {
    margin: 4px 0 0;
    font-size: 19px;
    letter-spacing: 0.6px;
    text-transform: uppercase;
  }
  .address {
    margin: 22px 0 0;
    font-size: 18px;
    line-height: 25px;
    font-style: normal;
  }
  .contact-list {
    list-style: none;
    margin: 14px 0 0;
    padding: 0;
    font-size: 18px;
  }
  .contact-list li {
    display: flex;
    align-items: center;
    height: 26px;
    white-space: nowrap;
  }
  .contact-list svg {
    width: 17px;
    height: 17px;
    margin-right: 11px;
    fill: var(--paper);
    flex: none;
  }

  .brand-lockup {
    position: absolute;
    left: 423px;
    top: 189px;
    display: flex;
    align-items: center;
  }
  .brand-dot {
    width: 66px;
    height: 66px;
    border: 9px solid var(--brand-blue);
    border-radius: 50%;
    box-sizing: border-box;
    margin-right: 18px;
  }
  .brand-name {
    font-family: "Cinzel", "Trajan Pro", serif;
    font-weight: 700;
    color: var(--brand-blue);
    line-height: 1;
  }
  .brand-name .line-1 { display: block; font-size: 40px; letter-spacing: 1px; }
  .brand-name .line-2 { display: block; font-size: 22px; letter-spacing: 7px; margin-top: 8px; }

  .back-lockup {
    position: absolute;
    left: 0;
    right: 0;
    top: 118px;
    display: flex;
    flex-direction: column;
    align-items: center;
  }
  .back-lockup .brand-dot {
    width: 150px;
    height: 150px;
    border-width: 20px;
    margin: 0 0 22px;
  }
  .back-lockup .brand-name { text-align: center; }
  .back-lockup .line-1 { font-size: 34px; letter-spacing: 2px; }
  .back-lockup .line-2 { font-size: 19px; letter-spacing: 8px; }
  .back-web {
    position: absolute;
    left: 0;
    right: 0;
    top: 401px;
    margin: 0;
    text-align: center;
    font-family: "EB Garamond", Georgia, serif;
    font-size: 18px;
    letter-spacing: 4px;
    color: var(--ink-grey);
  }
</style>
</head>
<body>
<div class="canvas">

  <section class="card card--front" aria-label="Business card front">
    <svg class="front-shape" viewBox="0 0 800 456" preserveAspectRatio="none" aria-hidden="true">
      <rect width="800" height="456" fill="var(--brand-blue)"/>
      <path d="M560 0 C 420 0 341 110 341 228 C 341 346 430 456 560 456 L800 456 L800 0 Z" fill="var(--paper)"/>
    </svg>

    <div class="contact-block">
      <h1 class="person-name">MARTIN E. CALDWELL</h1>
      <p class="person-title">Chairman, CEO</p>
      <address class="address">5120 Ridgemont Pkwy.<br>Suite 400, Atlanta, GA 30327</address>
      <ul class="contact-list">
        <li>
          <svg viewBox="0 0 24 24"><path d="M6.6 10.8a15.1 15.1 0 0 0 6.6 6.6l2.2-2.2c.3-.3.7-.4 1-.2 1.1.4 2.3.6 3.6.6.6 0 1 .4 1 1V20c0 .6-.4 1-1 1A17 17 0 0 1 3 4c0-.6.4-1 1-1h3.5c.6 0 1 .4 1 1 0 1.3.2 2.5.6 3.6.1.3 0 .7-.2 1z"/></svg>
          770.245.6274
        </li>
        <li>
          <svg viewBox="0 0 24 24"><path d="M7 1h10a2 2 0 0 1 2 2v18a2 2 0 0 1-2 2H7a2 2 0 0 1-2-2V3a2 2 0 0 1 2-2zm0 3v14h10V4zm5 15.5a1 1 0 1 0 0 2 1 1 0 0 0 0-2z"/></svg>
          404.617.2538
        </li>
        <li>
          <svg viewBox="0 0 24 24"><path d="M2 5h20v2l-10 6L2 7zm0 4 10 6 10-6v10H2z"/></svg>
          email@brantleyestates.com
        </li>
        <li>
          <svg viewBox="0 0 24 24"><path d="M12 2a10 10 0 1 0 0 20 10 10 0 0 0 0-20zm-1 17.9A8 8 0 0 1 4.1 11L9 16v1a2 2 0 0 0 2 2zm6.9-2.5A2 2 0 0 0 16 16h-1v-3a1 1 0 0 0-1-1H8v-2h2a1 1 0 0 0 1-1V7h2a2 2 0 0 0 2-2v-.4a8 8 0 0 1 2.9 12.8z"/></svg>
          www.brantleyestates.com
        </li>
      </ul>
    </div>

    <div class="brand-lockup">
      <span class="brand-dot" aria-hidden="true"></span>
      <span class="brand-name"><span class="line-1">BRANTLEY</span><span class="line-2">ESTATES</span></span>
    </div>
  </section>

  <section class="card card--back" aria-label="Business card back">
    <div class="back-lockup">
      <span class="brand-dot" aria-hidden="true"></span>
      <span class="brand-name"><span class="line-1">BRANTLEY</span><span class="line-2">ESTATES</span></span>
    </div>
    <p class="back-web">www.brantleyestates.com</p>
  </section>

</div>
</body>
</html>
```